Website Design for Forklift Training Company

DO NOT CONTACT PRIVATELY. ONLY SUBMISSIONS HERE WILL BE CONSIDERED

I need a design for a website that offers forklift training courses.

The company offers accredited, onsite forklift training that are customized for the needs of each individual company. The company offers a variety of courses to operate forklifts and other machinary.

About: "Pembrook Lift Academy Ltd delivers bespoke onsite forklift truck operator training throught the uk.
All our instructors have a wealth of knowledge and expertise to provide your company with all your forklift truck training requirements.
Pembrook Lift Academy Ltd is registered and accredited by qkmvd standards so you can be rest assured that all forklift training is carried out the very highest standard"

I need the following pages designed:
> a) Home Page: Include a header image, ways to contact, about snippet, overview of courses, accreditation that will be received after completing the courses. (See attachments for samples)
> b) About Page
> c) Contact Us Page
> d) Course Page Template: A page that will be used as template for the courses offered. It should contain;
1. Cover image for the course
2. A description of the course
3. A table indicating the various course options
4. Course Objectives
5. What the trainee will receive after doing the course (example: a certification)

Target Market(s)

Industrial Businesses

Number of Pages Required

4 page

Colors
0054AA
0677BA
7BADD7
CADEEF
E8F1F8
0094D4
00A9DD
6FCCEA
C7EBF8
E9F6FB

Requirements
Should not have
• - No Search bar

```html
<!DOCTYPE html>
<html lang="en">
<head>
<meta charset="utf-8">
<title>Forklift Course – Pembrook Lift Academy Ltd</title>
<link href="https://fonts.googleapis.com/css2?family=Montserrat:wght@300;400;500;600;700&family=Roboto+Condensed:wght@400&family=Roboto:wght@400;500&display=swap" rel="stylesheet">
<style>
:root{
  --navy:#0054AA;
  --blue:#0677BA;
  --sky:#0094D4;
  --cyan:#00A9DD;
  --pale:#E8F1F8;
  --mist:#EEF3F9;
  --ink:#1f2a3a;
  --text:#3b4654;
  --muted:#6c7480;
  --rule:#d9dde2;
  --dark:#2c3c4e;
  --white:#ffffff;
}
*{margin:0;padding:0;box-sizing:border-box}
html,body{width:1200px;height:3447px;overflow:hidden}
body{position:relative;background:var(--white);font-family:'Montserrat',sans-serif;color:var(--text)}
.abs{position:absolute}

/* hero */
.hero{position:absolute;left:0;top:0;width:1200px;height:520px;overflow:hidden}
.hero svg{position:absolute;left:0;top:0}
.brand{position:absolute;left:86px;top:8px;width:162px;text-align:center;color:var(--white)}
.brand-mark{width:46px;height:46px;border:3px solid var(--white);border-radius:50%;margin:0 auto 6px}
.brand-name{font-family:'Montserrat',sans-serif;font-weight:600;font-size:14px;letter-spacing:.3px;line-height:1.15}
.main-nav{position:absolute;top:25px;left:0;font-family:'Roboto Condensed',sans-serif;font-size:19px;color:var(--white)}
.main-nav a{position:absolute;color:var(--white);text-decoration:none;white-space:nowrap}
.main-nav a.active::after{content:"";position:absolute;left:0;right:0;bottom:-9px;height:2px;background:var(--white)}
.hero-kicker{position:absolute;left:83px;top:220px;font-weight:300;font-size:25px;letter-spacing:1.5px;color:var(--white)}
.hero-title{position:absolute;left:82px;top:256px;font-weight:700;font-size:45px;color:var(--white);letter-spacing:.5px}

/* description */
.desc-band{position:absolute;left:0;top:520px;width:1200px;height:691px;background:var(--mist)}
.desc-card{position:absolute;left:94px;top:590px;width:1012px;height:518px;background:var(--white);border:1px solid #cfd6de}
.desc-photo{position:absolute;left:0;top:0;width:506px;height:516px;background:linear-gradient(160deg,#c9ccc6 0%,#9aa4a7 40%,#5d6466 70%,#c8643a 88%,#8e8e88 100%)}
.desc-body{position:absolute;left:546px;top:60px;width:436px}
.desc-body h2{font-size:22px;font-weight:700;color:var(--navy);letter-spacing:.2px;margin-bottom:24px}
.desc-body h2 span{color:var(--sky)}
.desc-body p{font-size:12.2px;line-height:23px;color:var(--text);margin-bottom:23px}

/* section heads */
.kicker{position:absolute;left:0;width:1200px;text-align:center;font-family:'Roboto Condensed',sans-serif;font-size:16px;letter-spacing:2.5px;color:var(--ink)}
.section-title{position:absolute;left:0;width:1200px;text-align:center;font-weight:700;font-size:35px;color:var(--sky)}
.title-bar{position:absolute;height:4px;background:var(--sky)}

/* table */
.course-table{position:absolute;left:110px;top:1357px;width:974px;height:597px;border:1px solid #c8cdd3;border-top:none}
.course-table table{width:100%;border-collapse:collapse;font-family:'Roboto',sans-serif}
.course-table th{background:var(--dark);color:var(--white);font-family:'Montserrat',sans-serif;font-weight:600;font-size:12.5px;text-align:left;height:45px;padding:0}
.course-table td{height:30.8px;font-size:12px;color:var(--muted);border-bottom:1px solid #e3e6ea;padding:6px 0 0 0}
.course-table td.name{color:var(--ink);font-weight:500;padding-left:39px}
.course-table th.name{padding-left:38px}
.course-table tbody tr:first-child td{padding-top:14px;height:38px}

/* objectives */
.objectives{position:absolute;left:0;top:2051px;width:1200px;height:511px;background:linear-gradient(100deg,#0a63b4 0%,#1583cc 45%,#0d6fbf 100%)}
.objectives-bg{position:absolute;left:0;top:0;width:1200px;height:511px;background:radial-gradient(ellipse at 55% 40%,rgba(130,180,225,.35),transparent 60%)}
.objectives h2{position:absolute;left:0;top:56px;width:1200px;text-align:center;font-weight:700;font-size:24px;color:var(--white)}
.objectives .title-bar{background:var(--cyan);top:96px;left:570px;width:68px;height:3px}
.obj-card{position:absolute;top:135px;width:233px;height:266px;border:2px solid var(--white);padding:42px 22px 0 22px;color:var(--white);font-family:'Roboto',sans-serif}
.obj-card h3{font-size:14px;font-weight:500;line-height:20px;margin-bottom:17px}
.obj-card p{font-size:12px;line-height:15.5px}
.dots{position:absolute;top:2432px}
.dot{position:absolute;top:52px;height:3px;width:25px;background:rgba(255,255,255,.45)}
.dot.on{background:var(--white)}

/* certification */
.cert-band{position:absolute;left:0;top:2562px;width:1200px;height:702px;background:#eef4fb}
.cert-card{position:absolute;top:2788px;width:484px;height:379px;background:var(--white);border-radius:4px;box-shadow:0 4px 18px rgba(30,70,120,.07);font-family:'Roboto',sans-serif}
.badge{position:absolute;width:98px;height:96px}
.cert-card p{position:absolute;font-size:11.4px;line-height:21.6px;color:var(--text)}

/* footer */
.site-footer{position:absolute;left:0;top:3264px;width:1200px;height:183px;background:var(--dark);color:var(--white)}
.foot-nav a{position:absolute;top:43px;font-family:'Roboto Condensed',sans-serif;font-size:17px;color:var(--white);text-decoration:none}
.copyright{position:absolute;top:81px;left:0;width:1200px;text-align:center;font-family:'Roboto',sans-serif;font-size:11.5px;color:#aab4bf;letter-spacing:.2px}
.social{position:absolute;top:108px;width:22px;height:22px;border-radius:50%;background:var(--white)}
</style>
</head>
<body>

<header class="hero">
  <svg width="1200" height="520" viewBox="0 0 1200 520">
    <defs>
      <linearGradient id="heroBlue" x1="0" y1="0" x2="1" y2="1">
        <stop offset="0" stop-color="#0b3f8c"/>
        <stop offset=".55" stop-color="#1151a8"/>
        <stop offset="1" stop-color="#0a3a84"/>
      </linearGradient>
      <linearGradient id="heroPhoto" x1="0" y1="0" x2="1" y2="1">
        <stop offset="0" stop-color="#8d9aa3"/>
        <stop offset=".35" stop-color="#c9b83a"/>
        <stop offset=".6" stop-color="#e3c925"/>
        <stop offset=".85" stop-color="#6f6c5e"/>
        <stop offset="1" stop-color="#9a9a96"/>
      </linearGradient>
    </defs>
    <rect width="1200" height="520" fill="url(#heroBlue)" role="img" aria-label="Blue-tinted warehouse racking"/>
    <path d="M925 0 H1200 V520 H660 C760 360 850 170 925 0 Z" fill="url(#heroPhoto)" role="img" aria-label="Operator driving a yellow forklift truck in a warehouse"/>
    <path d="M905 0 C830 180 740 370 640 520" fill="none" stroke="#0f6fd0" stroke-width="16"/>
    <path d="M918 0 C842 185 752 375 652 520" fill="none" stroke="#ffffff" stroke-width="2.5"/>
    <path d="M880 0 C800 190 700 380 600 520" fill="none" stroke="#4a9ae8" stroke-width="1.5" opacity=".7"/>
  </svg>
  <div class="brand">
    <div class="brand-mark"></div>
    <div class="brand-name">Pembrook Lift Academy Ltd</div>
  </div>
  <nav class="main-nav">
    <a style="left:312px">HOME</a>
    <a class="active" style="left:413px">ABOUT US</a>
    <a style="left:547px">COURSES</a>
    <a style="left:671px">CONTACT US</a>
  </nav>
  <div class="hero-kicker">TRAINING COURSES</div>
  <h1 class="hero-title">FORKLIFT COURSE</h1>
</header>

<section class="desc-band"></section>
<div class="desc-card">
  <div class="desc-photo" role="img" aria-label="Trainee operating an electric pallet truck with an instructor in a warehouse"></div>
  <div class="desc-body">
    <h2>FORKLIFT COURSE <span>DESCRIPTION</span></h2>
    <p>Lorem Ipsum is simply dummy text of the printing and typesetting industry. Lorem Ipsum has been the industry's standard dummy text ever since the 1500s, when an unknown printer took a galley of type and scrambled it to make a type specimen book.</p>
    <p>It has survived not only five centuries, but also the leap into electronic typesetting, remaining essentially unchanged. It was popularised in the 1960s with the release of Letraset sheets containing Lorem Ipsum passages, and more recently with desktop publishing software like Aldus PageMaker including versions of Lorem Ipsumially unchanged. It was popularised in the 1960s with the release of Letraset sheets containing Lorem Ipsum passages, and more recently with desktop publishing software like Aldus PageMaker including versions of Lorem Ipsumially unchanged. It was popularised in the 1960s with the release of Letraset sheets containing Lorem Ipsum passages</p>
  </div>
</div>

<div class="kicker" style="top:1252px">WHAT WE OFFER</div>
<h2 class="section-title" style="top:1272px">COURSE TABLE</h2>
<div class="title-bar" style="left:560px;top:1320px;width:80px"></div>

<div class="course-table">
  <table>
    <colgroup><col style="width:354px"><col style="width:310px"><col></colgroup>
    <thead><tr><th class="name">COURSE TITLE</th><th>TITLE HERE</th><th>DESCRIPTION</th></tr></thead>
    <tbody>
      <tr><td class="name">Benton Truck Training Course</td><td>Lorem Ipsum is</td><td>Lorem Ipsum is simply</td></tr>
      <tr><td class="name">Corvan Lift Training course</td><td>Dummy text of</td><td>Dummy text of the printing and</td></tr>
      <tr><td class="name">Counterbalance Training Course</td><td>Typesetting industry</td><td>Typesetting industry</td></tr>
      <tr><td class="name">Fenwyn Truck Training Course</td><td>Lorem Ipsum</td><td>Lorem Ipsum has been the</td></tr>
      <tr><td class="name">Harlow Crane Training Course</td><td>Industry's standard</td><td>Industry's standard</td></tr>
      <tr><td class="name">Llop Training Course</td><td>Dummy text ever</td><td>Dummy text ever since</td></tr>
      <tr><td class="name">Mortlake Truck Training Course</td><td>Lorem Ipsum is</td><td>Lorem Ipsum is simply</td></tr>
      <tr><td class="name">Order Picker Truck Training Course</td><td>Dummy text of</td><td>Dummy text of the printing and</td></tr>
      <tr><td class="name">Pedestrian Training Course</td><td>Typesetting industry</td><td>Typesetting industry</td></tr>
      <tr><td class="name">Pivot Steer Training Course</td><td>Lorem Ipsum</td><td>Lorem Ipsum has been the</td></tr>
      <tr><td class="name">Reach Training Course</td><td>Industry's standard</td><td>Industry's standard</td></tr>
      <tr><td class="name">Rough Terrain Training Course</td><td>Dummy text ever</td><td>Dummy text ever since</td></tr>
      <tr><td class="name">Sideloader Training Course</td><td>Lorem Ipsum is</td><td>Lorem Ipsum is simply</td></tr>
      <tr><td class="name">Telescopic Handeler Training Course</td><td>Dummy text of</td><td>Dummy text of the printing and</td></tr>
      <tr><td class="name">Tow Tractor Training Course</td><td>Typesetting industry</td><td>Typesetting industry</td></tr>
      <tr><td class="name">Vna Man Down&nbsp; Truck Training Course</td><td>Lorem Ipsum</td><td>Lorem Ipsum has been the</td></tr>
      <tr><td class="name">Vna Man Up Truck Training Course</td><td>Industry's standard</td><td>Industry's standard</td></tr>
    </tbody>
  </table>
</div>

<section class="objectives">
  <div class="objectives-bg" role="img" aria-label="Faint blue-toned warehouse training scene"></div>
  <h2>COURSE OBJECTIVES</h2>
  <div class="title-bar"></div>
  <div class="obj-card" style="left:119px"><h3>Lorem Ipsum is simply dummy text of the printing</h3><p>typesetting industry. Lorem Ipsum has been the industry's standard dummy text ever since the 1500sstry. Lorem Ipsum has been the industry's standard dummy text ever since the 1500sstry. Lorem Ipsum has been the industry's standard dummy text ever since the 1500s,</p></div>
  <div class="obj-card" style="left:365px"><h3>Lorem Ipsum is simply dummy text of the printing</h3><p>typesetting industry. Lorem Ipsum has been the industry's standard dummy text ever since the 1500sstry. Lorem Ipsum has been the industry's standard dummy text ever since the 1500sstry. Lorem Ipsum has been the industry's standard dummy text ever since the 1500s,</p></div>
  <div class="obj-card" style="left:609px"><h3>Lorem Ipsum is simply dummy text of the printing</h3><p>typesetting industry. Lorem Ipsum has been the industry's standard dummy text ever since the 1500sstry. Lorem Ipsum has been the industry's standard dummy text ever since the 1500sstry. Lorem Ipsum has been the industry's standard dummy text ever since the 1500s,</p></div>
  <div class="obj-card" style="left:855px"><h3>Lorem Ipsum is simply dummy text of the printing</h3><p>typesetting industry. Lorem Ipsum has been the industry's standard dummy text ever since the 1500sstry. Lorem Ipsum has been the industry's standard dummy text ever since the 1500sstry. Lorem Ipsum has been the industry's standard dummy text ever since the 1500s,</p></div>
</section>
<div class="dots">
  <span class="dot on" style="left:564px"></span>
  <span class="dot" style="left:599px"></span>
</div>

<section class="cert-band"></section>
<div class="kicker" style="top:2612px">WHAT YOU GET AFTER COURSE</div>
<h2 class="section-title" style="top:2638px;font-size:26px">CERTIFICATION RECEIVED</h2>
<div class="title-bar" style="left:570px;top:2676px;width:68px;height:3px"></div>
<svg class="abs" style="left:320px;top:2682px" width="580" height="100" viewBox="0 0 580 100">
  <path d="M277 2 V30 C277 45 265 50 250 50 H40 C22 50 8 62 8 80 V96" fill="none" stroke="#c4d7ec" stroke-width="2"/>
  <path d="M297 2 V30 C297 45 309 50 324 50 H534 C552 50 566 62 566 80 V96" fill="none" stroke="#c4d7ec" stroke-width="2"/>
</svg>

<div class="cert-card" style="left:116px">
  <div class="badge" style="left:32px;top:30px;background:var(--navy)" role="img" aria-label="qkmvd accreditation badge"></div>
  <p style="left:35px;top:148px;width:425px">qkmvd is recognised throughout the united kingdom and Ireland as one of the leading material handling equipment training accrediting bodies. qkmvd is a founder member of the CBA (accrediting bodies association for workplace transport) and this replaced the accrediting bodies forum previously run by the NSB. They have over 40 years experience of setting training standards,accreditation and monitoring. The qkmvd accreditation schemes are supported by legal requirements for training.</p>
</div>
<div class="cert-card" style="left:617px">
  <div class="badge" style="left:36px;top:30px;width:120px;height:76px;border-radius:6px;background:#4f8f3a" role="img" aria-label="CBA workplace transport badge"></div>
  <p style="left:32px;top:138px;width:428px">We are accredited by the qkmvd who are recognised by the national workplace safety board as competent to deliver forklift truck operator training courses. As an qkmvd accredited training provider we are monitored annually to ensure we are maintaining our high standards as laid down by the qkmvd. All our instructors are qualified and registered with the qkmvd and monitored. Please note we are only accredited to deliver training at customer premises as we do not have a training centre.</p>
</div>

<footer class="site-footer">
  <nav class="foot-nav">
    <a style="left:355px">HOME</a>
    <a style="left:468px">ABOUT US</a>
    <a style="left:606px">COURSES</a>
    <a style="left:740px">CONTACT US</a>
  </nav>
  <div class="copyright">2020 © COPYRIGHT PEMBROOK LIFT ACADEMY LTD RIGHTS RESERVED.</div>
  <span class="social" style="left:557px" aria-label="Social link"></span>
  <span class="social" style="left:586px" aria-label="Social link"></span>
  <span class="social" style="left:614px" aria-label="Social link"></span>
</footer>

</body>
</html>
```